Home Design company focused on remodel and enhancement of kitchens and bathroorms

I already have a logo designed by ArtHarbor, I now need a design for my business cards.
The company is in the remodeling and enhancement industry for homes, focusing on kitchens and bathrooms, however, we can remodel or enhance every room in a home, an office space, etc.

The company's name is VELMOR HOME DESIGN, LLC

We'll focus on clients in the Rio Grande Valley, Texas. Primarily McAllen, Edinburg, Pharr, Mission, Brownsville and South Padre Island.

The design on the business card should transmit reliability, professionalism anda bit of upscale design.

The logo is in black and white, and would like to keep it that way.

The information that needs to be printed in the business cards is:
Company's name: Velmor Home Design
Company's Logo (attached)
My name: Noel Bramwit
Address, phone and email:
2715 N Parkline Road, Ste 348
Brenmoor, TX 70419
(555) 555 0187
nbramwit@velmordesign.example
Website: velmordesign.example

```html
<!DOCTYPE html>
<html lang="en">
<head>
<meta charset="utf-8">
<title>Velmor Home Design — Business Card</title>
<link rel="stylesheet" href="https://fonts.googleapis.com/css2?family=Montserrat:wght@400;700&family=Arimo:wght@400&display=swap">
<style>
  :root {
    --page: #d9d9d9;
    --ink: #111111;
    --paper: #ffffff;
    --card-dark: #161616;
    --emboss: #3a3a3a;
  }
  * { box-sizing: border-box; margin: 0; padding: 0; }
  html, body { width: 1200px; height: 960px; overflow: hidden; }
  body {
    background: var(--page);
    display: flex;
    flex-direction: column;
    align-items: center;
    justify-content: center;
    gap: 60px;
  }
  .card {
    position: relative;
    width: 700px;
    height: 400px;
    overflow: hidden;
    box-shadow: 0 10px 30px rgba(0,0,0,.25);
  }
  .card--back { background: var(--card-dark); }
  .card--front { background: var(--paper); }

  .brand {
    display: flex;
    align-items: center;
    gap: 14px;
    font-family: "Montserrat", sans-serif;
    font-weight: 400;
    letter-spacing: .3em;
    line-height: 1.15;
    text-transform: uppercase;
  }
  .brand__mark { width: 14px; height: 14px; flex: none; }
  .brand__rule { width: 1px; align-self: stretch; flex: none; }
  .card--back .brand {
    position: absolute;
    left: 50%; top: 50%;
    transform: translate(-50%, -50%);
    color: var(--emboss);
    font-size: 26px;
  }
  .card--back .brand__mark { background: var(--emboss); width: 20px; height: 20px; }
  .card--back .brand__rule { background: var(--emboss); }
  .card--front .brand {
    position: absolute;
    right: 52px; top: 48px;
    color: var(--ink);
    font-size: 14px;
  }
  .card--front .brand__mark { background: var(--ink); }
  .card--front .brand__rule { background: var(--ink); }

  .house { position: absolute; inset: 0; }

  .contact {
    position: absolute;
    left: 60px; top: 196px;
    font-family: "Arimo", sans-serif;
    color: var(--ink);
    font-size: 15px;
    line-height: 1.3;
  }
  .contact__name {
    font-family: "Montserrat", sans-serif;
    font-weight: 700;
    font-size: 21px;
    letter-spacing: .08em;
    text-transform: uppercase;
    margin-bottom: 10px;
  }
  .contact__address { margin-bottom: 12px; }
  .contact__list { list-style: none; }
  .contact__list li { display: flex; align-items: center; gap: 12px; }
  .contact__list svg { width: 13px; height: 13px; flex: none; }
</style>
</head>
<body>

  <section class="card card--back" aria-label="Card back">
    <div class="brand"><span class="brand__mark"></span><span class="brand__rule"></span><span>Velmor<br>Home<br>Design</span></div>
  </section>

  <section class="card card--front" aria-label="Card front">
    <svg class="house" viewBox="0 0 700 400" aria-hidden="true">
      <polyline points="-20,190 150,72 470,72 520,130 520,410"
                fill="none" stroke="#111" stroke-width="24" stroke-linejoin="miter"/>
    </svg>

    <div class="brand"><span class="brand__mark"></span><span class="brand__rule"></span><span>Velmor<br>Home<br>Design</span></div>

    <div class="contact">
      <p class="contact__name">Noel Bramwit</p>
      <p class="contact__address">2715 N Parkline Road, Ste 348<br>Brenmoor, TX 70419</p>
      <ul class="contact__list">
        <li>
          <svg viewBox="0 0 24 24"><path fill="#111" d="M6.6 10.8a15 15 0 0 0 6.6 6.6l2.2-2.2c.3-.3.7-.4 1-.2 1.1.4 2.3.6 3.6.6.6 0 1 .4 1 1V20c0 .6-.4 1-1 1A17 17 0 0 1 3 4c0-.6.4-1 1-1h3.5c.6 0 1 .4 1 1 0 1.3.2 2.5.6 3.6.1.3 0 .7-.2 1z"/></svg>
          (555) 555 0187
        </li>
        <li>
          <svg viewBox="0 0 24 24"><rect x="2" y="5" width="20" height="14" fill="#111"/><polyline points="2,6 12,13 22,6" fill="none" stroke="#fff" stroke-width="2"/></svg>
          nbramwit@velmordesign.example
        </li>
        <li>
          <svg viewBox="0 0 24 24"><circle cx="12" cy="12" r="10" fill="#111"/><path d="M2 12h20M12 2c3 3 3 17 0 20M12 2c-3 3-3 17 0 20" fill="none" stroke="#fff" stroke-width="1.4"/></svg>
          www.velmordesign.example
        </li>
      </ul>
    </div>
  </section>

</body>
</html>
```